Chateau de Verbouclin multiple flyers

PRICE OFFERED IS PER FLYER IE: €139 PER FLYER OR €695 TOTAL WITH OTHERS TO FOLLOW

I want to creat a common design across a range of flyers that I will be handing out to visitors to our Christmas market, but will also be used throughout the year and years to come. The final design will need to be adapted so the copy can be translated into french as well as English. So I would need an ai or paint version as well as pdf's etc.

There are 5 flyers to be designed at this stage the PRICE OFFERED IS PER FLYER IE: €139 PER FLYER OR €695 TOTAL WITH OTHERS TO FOLLOW

1. Seminars at the chateau - 4 page 1/3 A4 double sided (No longer referring to full chateau rental)
2. Accomodation at the chateau 2 page 1/3 A4 double sided (Seasons simplified now: Peak = July & August and Christmas week; High, June and September. Low: Rest of year.)
3. VQEB 2 Diploma in Cellar Studies 4 page 1/3 A4 double sided
See current offering at
http://www.vinharbour-example.com/experiences-and-tours/wine-tours/vqeb-level-2-loire-valley-peter-anwick/#1467282665644-f1124b7e-5513

With photos here:
https://www.filecrate-example.com/sh/qpz481bnrtkaye/BBBQ9nyJRLfuF-Bdfy6thwwjb?dl=0

4. Valentine's/Romantic package 2 page 1/3 A4 double sided
5. Mothers Day package 2 page 1/3 A4 double sided.

The first two are very urgent as need to be available by Wednesday 7th December to go to print.

In the future we will be looking to add to the range with:

6. Wedding Brochure - 6 page 1/3 A4 double sided
7. Group celebrations - 6 page 1/3 A4 double sided
8. Pamper/Wellness package - 2 page 1/3 A4 double sided
9. Activity Break - 2 page 1/3 A4 double sided.

I have attached some examples of what we have to date, which are not consistent. As well as some excel spreadhseets which explain the packages. Along with an architects plan of the ground floor (may help with the seminar brochure.)

I have also provided a link to our gallery of photos that can be used and a couple of videos to give you a feel for the place.

https://www.filecrate-example.com/sh/k7rbtwqogrdhz/BBDGNXBuSplm7BHRdgbUyKb?dl=0

Target Market(s)

Adults aged 34 plus.
Seminars = Local businesses
Accommodation = 34 plus high income
Wedding = Females 28 plus high income

Requirements
Must have
• Demonstrates 5 star luxury and quality.

```html
<!DOCTYPE html>
<html lang="en">
<head>
<meta charset="utf-8">
<title>Chateau de Verbouclin – Accommodation Price List</title>
<link rel="stylesheet" href="https://fonts.googleapis.com/css2?family=Lato:wght@400;700&family=Libre+Baskerville&display=swap">
<style>
  :root {
    --maroon: #5d1414;
    --maroon-text: #6b1717;
    --charcoal: #333333;
    --page: #ffffff;
    --paper: #fbfafa;
    --taupe: #c8ab9c;
    --taupe-light: #dccdc6;
    --grey-row: #e5e3e2;
    --ink: #1e1e1e;
    --cream: #efe3d6;
  }
  * { box-sizing: border-box; margin: 0; padding: 0; }
  html, body { width: 1200px; height: 1029px; overflow: hidden; background: var(--page); }
  body { position: relative; font-family: "Lato", sans-serif; color: var(--ink); }

  .flyer { position: absolute; background: var(--paper); box-shadow: 0 2px 6px rgba(0,0,0,.18); overflow: hidden; }
  .footer-band { position: absolute; left: 0; right: 0; bottom: 0; background: var(--charcoal); }

  .brand { position: absolute; text-align: center; color: var(--cream);
    font-family: "Lato", sans-serif; font-weight: 400; font-size: 9px; letter-spacing: 2.6px; text-transform: uppercase; white-space: nowrap; }

  /* Price list card */
  .price-card { left: 19px; top: 335px; width: 759px; height: 369px; }
  .price-card .corner { position: absolute; left: 0; top: 0; }
  .price-card .brand { left: 16px; top: 66px; width: 170px; }
  .price-card .footer-band { height: 20px; }
  .title { position: absolute; left: 300px; width: 306px; top: 20px; text-align: center;
    font-family: "Libre Baskerville", serif; font-weight: 400; color: var(--maroon-text); font-size: 45px; letter-spacing: 1px; }
  .subtitle { position: absolute; left: 300px; width: 306px; top: 80px; text-align: center;
    font-family: "Libre Baskerville", serif; font-size: 19px; color: var(--ink); }

  .season { position: absolute; top: 124px; width: 120px; margin-left: -60px; text-align: center;
    font-weight: 700; font-size: 14px; color: var(--maroon-text); }

  .rate-grid { position: absolute; left: 42px; width: 677px; display: grid;
    grid-template-columns: 189px 47px 60px 51px 48px 56px 60px 47px 60px 1fr; align-items: center; font-size: 13px; }
  .rate-grid .val { display: flex; justify-content: center; width: 0; white-space: nowrap; position: relative; }
  .rate-head { top: 148px; height: 20px; }
  .rate-head::before { content: ""; position: absolute; left: 149px; right: 4px; top: 0; bottom: 0; background: var(--grey-row); border-radius: 4px; }
  .rate-head .val { color: var(--maroon-text); }
  .rate-body { top: 173px; height: 154px; background: var(--grey-row); border-radius: 6px; overflow: hidden;
    grid-auto-rows: 29px; padding: 2px 0; }
  .rate-body::before { content: ""; position: absolute; left: 0; top: 0; bottom: 0; width: 149px; background: var(--taupe); }
  .rate-body .room { position: relative; padding-left: 22px; white-space: nowrap; }

  /* Info card */
  .info-card { left: 800px; top: 139px; width: 381px; height: 783px; }
  .info-card .photo { position: absolute; left: 0; top: 0; width: 381px; height: 380px;
    background: linear-gradient(180deg, #8fae5a 0%, #6e9a48 36%, #3f9cc0 40%, #2f86b4 70%, #4a7fa3 100%); }
  .info-card .header-shape { position: absolute; left: 0; top: 0; }
  .info-card .brand { left: 22px; top: 67px; width: 170px; }
  .info-card .footer-band { height: 13px; }
  .inset { position: absolute; width: 104px; height: 104px; border-radius: 50%; border: 4px solid var(--maroon); }
  .inset-stairs { left: 5px; top: 273px; background: linear-gradient(135deg, #d9c5ad, #9c7e63); }
  .inset-tower { left: 100px; top: 273px; background: linear-gradient(180deg, #7fb1d8 0%, #b9ad98 45%, #8d7e6c 100%); }

  .season-table { position: absolute; left: 34px; top: 405px; width: 323px; font-size: 13px; }
  .season-row { display: grid; grid-template-columns: 143px 1fr; margin-bottom: 2px; }
  .season-row dt { background: var(--taupe-light); padding: 2px 0 1px 14px; font-weight: 700; line-height: 20.5px; }
  .season-row dd { background: var(--grey-row); text-align: left; padding: 2px 0 1px 56px; line-height: 20.5px; white-space: nowrap; }
  .season-row:first-child dd { padding-left: 56px; }

  .contact { position: absolute; left: 0; width: 381px; top: 644px; height: 109px; text-align: center; font-size: 13px; line-height: 19px;
    padding-top: 14px; font-style: normal;
    box-shadow: inset 0 6px 6px -6px rgba(0,0,0,.15), inset 0 -6px 6px -6px rgba(0,0,0,.15); }
  .contact .name { font-family: "Libre Baskerville", serif; color: var(--maroon-text); text-transform: uppercase; font-size: 13px; letter-spacing: .5px; }
  .contact .label { color: var(--maroon-text); }
</style>
</head>
<body>

<section class="flyer price-card">
  <svg class="corner" width="300" height="130" viewBox="0 0 300 130" aria-hidden="true">
    <path d="M0 0 H284 C242 70 162 118 0 126 Z" fill="#333333"/>
    <path d="M0 0 H272 C230 66 152 112 0 120 Z" fill="#5d1414"/>
  </svg>
  <div class="brand">Chateau de Verbouclin</div>

  <h1 class="title">PRICE LIST</h1>
  <p class="subtitle">Accomodation</p>

  <div class="season" style="left:294px">Low season</div>
  <div class="season" style="left:445px">High season</div>
  <div class="season" style="left:595px">Peak season</div>

  <div class="rate-grid rate-head">
    <span></span><span class="val">Wday</span><span class="val">WE</span><span class="val">Week</span><span class="val">Wday</span><span class="val">WE</span><span class="val">Week</span><span class="val">Wday</span><span class="val">WE</span><span class="val">Week</span>
  </div>

  <div class="rate-grid rate-body">
    <span class="room">Studio</span><span class="val">€115</span><span class="val">€150</span><span class="val">€875</span><span class="val">€140</span><span class="val">€180</span><span class="val">€1060</span><span class="val">€165</span><span class="val">€215</span><span class="val">€1255</span>
    <span class="room">One-bedroom Suite</span><span class="val">€130</span><span class="val">€165</span><span class="val">€980</span><span class="val">€155</span><span class="val">€200</span><span class="val">€1175</span><span class="val">€185</span><span class="val">€235</span><span class="val">€1395</span>
    <span class="room">Two-bedroom Suite</span><span class="val">€225</span><span class="val">€285</span><span class="val">€1695</span><span class="val">€270</span><span class="val">€350</span><span class="val">€2050</span><span class="val">€320</span><span class="val">€405</span><span class="val">€2410</span>
    <span class="room">Clock Tower</span><span class="val">€305</span><span class="val">€365</span><span class="val">€2255</span><span class="val">€350</span><span class="val">€430</span><span class="val">€2610</span><span class="val">€400</span><span class="val">€485</span><span class="val">€2970</span>
    <span class="room">Whole Chateau</span><span class="val">€2300</span><span class="val">€2900</span><span class="val">€16000</span><span class="val">€2800</span><span class="val">€3500</span><span class="val">€19000</span><span class="val">€3300</span><span class="val">€4100</span><span class="val">€23000</span>
  </div>

  <div class="footer-band"></div>
</section>

<section class="flyer info-card">
  <div class="photo" role="img" aria-label="Poolside table with a champagne bottle, glasses and fruit beside a lawn"></div>
  <svg class="header-shape" width="381" height="380" viewBox="0 0 381 380" aria-hidden="true">
    <path d="M0 0 H294 C252 78 162 126 0 130 Z" fill="#333333"/>
    <path d="M0 0 H282 C240 72 152 120 0 124 Z" fill="#5d1414"/>
    <path d="M60 345 C160 350 280 330 381 318 V380 H0 V330 Z" fill="#5d1414"/>
    <path d="M60 355 C160 360 280 342 381 330 V380 H0 V340 Z" fill="#fbfafa"/>
  </svg>
  <div class="brand">Chateau de Verbouclin</div>
  <div class="inset inset-stairs" role="img" aria-label="Curved stone staircase with wrought iron railing"></div>
  <div class="inset inset-tower" role="img" aria-label="Stone clock tower of the chateau"></div>

  <dl class="season-table">
    <div class="season-row"><dt>Weekday rate:<br>Weekend rate:</dt><dd>Sunday to Thursday<br>Friday and Saturday</dd></div>
    <div class="season-row"><dt>Low season:</dt><dd>03.01.—04.04.<br>01.11.—19.02.</dd></div>
    <div class="season-row"><dt>High season:</dt><dd>05.04.—30.05.<br>07.06.—27.06.<br>06.09.—17.10.</dd></div>
    <div class="season-row"><dt>Peak season:</dt><dd>31.05.—06.06.<br>28.06.—05.09.<br>20.12.—02.01.</dd></div>
  </dl>

  <address class="contact">
    <div class="name">Chateau de Verbouclin</div>
    <div>verbouclin, Rue des Tilleuls, 37990</div>
    <div><span class="label">Phone:</span> +33 (0) 2 99 72 38 14</div>
    <div><span class="label">Website:</span> www.chateaudeverbouclin.fr</div>
    <div><span class="label">E-mail:</span> gm@chateaudeverbouclin.fr</div>
  </address>

  <div class="footer-band"></div>
</section>

</body>
</html>
```